Refer a Friend A5 Flyer for Healthcare Staff

We need an A5 flyer that we can hand out to existing and new staff members promoting our Refer a friend Scheme. We need the leaflet to encourage staff to talk to their family and friends about joining our Healthcare Agency, which provides staff to local care related establishments. Using our logo and brand colours blue and green, as per our website, the final design will need to clearly convey the benefits and attractions of referring additional staff to the team. In addition is the promotion of our Chatterbox page, requesting staff to like the page and to like and share various posts.

Target Market(s)

Healthcare and potential Healthcare Staff

Industry/Entity Type

Healthcare

Colors
33b8a4
3277b5

Requirements
Must have
• Company Logo, Brand colours,
• text; "Refer a Friend and receive a £50 Bonus after just 1 completed shift"
• text; "3 easy steps to refer a friend, 1 Fill out your name on the back of your Business Card 2 Hand the card to your friend or any person you wish to refer, 3 ask your friend to present the card to us when they attend their interview"
• text; "Like and share any of our Open Days on Chatterbox for a chance to win a prize, you can find us easily by searching @CareBridgeStaffing"
• text; "Like our Page to stay up to date with our events and offers"
Nice to have
• care worker / elderly care / support worker pictures
• Content / pics from website www.carebridgestaffing.co.uk

```html
<!DOCTYPE html>
<html lang="en">
<head>
<meta charset="utf-8">
<title>CareBridge Staffing – Refer a Friend</title>
<link rel="stylesheet" href="https://fonts.googleapis.com/css2?family=Poppins:ital,wght@0,300;0,400;0,500;0,700;1,400&family=Bebas+Neue&family=Roboto+Condensed:wght@400&display=swap">
<style>
  :root {
    --brand-blue: #0f55a5;
    --brand-blue-dark: #0d4a92;
    --brand-green: #1ba98d;
    --brand-green-light: #4cc3ac;
    --paper: #ffffff;
    --backdrop: #e9e7e4;
  }
  * { box-sizing: border-box; margin: 0; padding: 0; }
  html, body { width: 1099px; height: 1200px; overflow: hidden; }
  body {
    background: var(--backdrop);
    font-family: "Poppins", sans-serif;
    position: relative;
  }
  .flyer {
    position: absolute;
    left: 135px; top: 12px;
    width: 828px; height: 1175px;
    background: var(--paper);
    box-shadow: 0 2px 10px rgba(0,0,0,.18);
    overflow: hidden;
  }
  .hero-photo {
    position: absolute; left: 0; top: 0;
    width: 450px; height: 393px;
    background: linear-gradient(160deg, #6f8f4a 0%, #3f6b2e 40%, #b3593f 65%, #8a7d55 100%);
  }
  .brand {
    position: absolute; left: 478px; top: 160px; width: 330px;
  }
  .brand-name {
    font-size: 34px; font-weight: 400; color: var(--brand-blue);
    line-height: 1.1; white-space: nowrap;
  }
  .values { position: absolute; left: 455px; top: 293px; width: 373px; }
  .value-row { position: relative; height: 30px; margin-bottom: 5px; }
  .value-row::after {
    content: ""; position: absolute; left: 0; right: 0; top: 1px; bottom: 1px;
    background: var(--brand-blue); z-index: 0;
  }
  .value-label {
    position: relative; z-index: 1; display: inline-block; height: 30px;
    background: var(--brand-green); color: #fff;
    font-size: 25px; font-weight: 400; line-height: 32px;
    padding: 0 4px; border-right: 3px solid #fff;
  }
  .offer-band {
    position: absolute; left: 0; top: 397px; width: 828px; height: 268px;
    background: var(--brand-blue);
    color: #fff; text-align: center;
    padding-top: 34px;
    font-size: 58px; font-weight: 500; line-height: 63px;
  }
  .offer-band strong { font-weight: 700; }
  .team-photo {
    position: absolute; left: 60px; top: 705px;
    width: 185px; height: 200px;
    background: radial-gradient(ellipse at 50% 45%, #c9d6e6 0%, #e7eef6 60%, #fff 100%);
  }
  .steps { position: absolute; left: 272px; top: 718px; width: 540px; }
  .steps-title {
    font-family: "Bebas Neue", sans-serif;
    font-size: 47px; color: var(--brand-blue-dark); line-height: 1;
    white-space: nowrap; font-weight: 400;
  }
  .step-list { list-style: none; margin-top: 14px; }
  .step {
    display: flex; align-items: flex-start; gap: 8px;
    font-family: "Roboto Condensed", sans-serif;
    font-size: 19.5px; color: var(--brand-blue); line-height: 24px;
    margin-bottom: 5px;
  }
  .step-num {
    flex: none; width: 17px; height: 17px; margin-top: 4px;
    border: 1.5px solid var(--brand-green); border-radius: 50%;
    font-size: 10px; line-height: 14px; text-align: center; color: var(--brand-blue);
  }
  .social-box {
    position: absolute; left: 30px; top: 948px; width: 763px; height: 194px;
    border: 5px solid var(--brand-blue); border-radius: 12px;
    overflow: hidden; background: var(--brand-green);
  }
  .social-main {
    height: 135px;
    background: linear-gradient(180deg, var(--brand-green-light) 0%, var(--brand-green) 55%, #15a288 100%);
    color: #fff; text-align: center;
    font-size: 28px; line-height: 34px; padding-top: 12px;
  }
  .social-main strong { font-weight: 700; }
  .social-footer {
    height: 54px; background: linear-gradient(180deg, var(--brand-blue) 0%, #4f86c4 100%);
    color: #fff; text-align: center;
    font-size: 24px; font-style: italic; line-height: 46px;
  }
</style>
</head>
<body>
  <main class="flyer">
    <div class="hero-photo" role="img" aria-label="Smiling care worker with an elderly woman in a wheelchair in a garden"></div>

    <div class="brand">
      <div class="brand-name">CareBridge Staffing</div>
    </div>

    <div class="values">
      <div class="value-row"><span class="value-label">SIMPLICITY</span></div>
      <div class="value-row"><span class="value-label">SUPERIOR SOLUTIONS</span></div>
      <div class="value-row"><span class="value-label">OFFICIALLY RECOGNIZED</span></div>
    </div>

    <section class="offer-band">
      Refer a Friend and<br>
      receive a <strong>£50</strong> Bonus after<br>
      just 1 completed shift
    </section>

    <div class="team-photo" role="img" aria-label="Group of healthcare staff in uniforms joining hands"></div>

    <section class="steps">
      <h2 class="steps-title">3 Easy Steps to Refer a Friend</h2>
      <ol class="step-list">
        <li class="step"><span class="step-num">1</span><span>Fill out your name on the back of your Business Card</span></li>
        <li class="step"><span class="step-num">2</span><span>Hand the card to your friend or any person you wish to refer</span></li>
        <li class="step"><span class="step-num">3</span><span>ask your friend to present the card to us when they<br>attend their interview</span></li>
      </ol>
    </section>

    <section class="social-box">
      <div class="social-main">
        Like and share any of our Open Days on <strong>Chatterbox</strong><br>
        for a chance to win a prize, you can find us easily<br>
        by searching <strong>@CareBridgeStaffing</strong>
      </div>
      <div class="social-footer">Like our Page to stay up to date with our events and offers</div>
    </section>
  </main>
</body>
</html>
```